Renewable energy website needs a wordpress website

We are a Renewable Energy company specialising in Energy Management, LED Lights and Solar PV Systems based in Kuala Lumpur.
We need wordpress website designed to match our company identity.
We would like to stick with similar shades of blue & green as our logo and to keep it fresh and creative at the same time.

```html
<!DOCTYPE html>
<html lang="en">
<head>
<meta charset="utf-8">
<title>Verdant Current – Renewable Energy</title>
<link href="https://fonts.googleapis.com/css2?family=Questrial&display=swap" rel="stylesheet">
<style>
:root{
  --blue:#1fb0e4;
  --blue-deep:#1b8fd6;
  --blue-text:#2aa7df;
  --green:#6fa83e;
  --green-dark:#54882a;
  --green-text:#7cbf3a;
  --paper:#f2f2f2;
  --linen:#e1e1e1;
  --band:#cfcfcf;
  --ink:#666;
  --ink-soft:#8a8a8a;
  --white:#fff;
  --foot-top:#3b3b3b;
  --foot-bottom:#171717;
}
*{margin:0;padding:0;box-sizing:border-box}
html,body{width:977px;height:1200px;overflow:hidden}
body{position:relative;font-family:"Questrial",sans-serif;background:var(--linen);color:var(--ink)}
.abs{position:absolute}

.topbar{left:0;top:0;width:977px;height:27px;background:var(--blue);color:var(--white);font-size:14px}
.topbar .contacts{position:absolute;right:48px;top:0;height:27px;display:flex;align-items:center;gap:18px;white-space:nowrap}
.topbar .contact{display:flex;align-items:center;gap:6px}
.header{left:0;top:27px;width:977px;height:316px;background:var(--paper)}
.brand{left:46px;top:50px;display:flex;align-items:center;gap:10px}
.brand .dot{width:40px;height:40px;border-radius:50%;background:var(--blue)}
.brand .name{font-size:17px;letter-spacing:2px;color:var(--blue);line-height:1}

.social{left:828px;width:113px;height:19px;color:var(--white);font-size:8px;display:flex;align-items:center;gap:6px;white-space:nowrap}
.social .sq{width:19px;height:19px;background:rgba(0,0,0,.15)}
.social.page{top:40px;background:#5a74a8}
.social.updates{top:65px;background:#1fa8e6}
.social.feed{top:90px;background:#f5a02a}

.nav{left:40px;top:122px;width:901px;height:34px;background:linear-gradient(#82b84d,#5f9a32);display:flex;align-items:center}
.nav a{position:absolute;color:var(--white);text-decoration:none;font-size:13.5px;letter-spacing:1px;white-space:nowrap}

.hero{left:40px;top:156px;width:901px;height:262px;background:linear-gradient(180deg,#178ad6,#38b2ea);overflow:hidden}
.hero-shadow{left:60px;top:416px;width:860px;height:30px;border-radius:50%;box-shadow:0 12px 18px rgba(0,0,0,.25)}
.welcome{left:568px;top:35px;width:300px;text-align:center;color:var(--white)}
.welcome .kicker{font-size:13px;letter-spacing:1px}
.welcome .name{margin-top:14px;font-size:17px;letter-spacing:2px;display:flex;justify-content:center;align-items:center;gap:8px;white-space:nowrap}
.welcome .name .dot{width:30px;height:30px;border-radius:50%;background:var(--white);opacity:.9}
.welcome p{margin-top:18px;font-size:13px;line-height:16.5px;letter-spacing:.4px}
.dots{left:765px;top:235px;display:flex;gap:3px}
.dots span{width:12px;height:12px;border-radius:50%;background:#8fd3f5}
.dots span.on{background:var(--white)}

.features{left:40px;top:451px;width:901px;height:306px}
.divider{top:0;width:1px;height:240px;background:#cdcdcd}
.feature{top:18px;width:200px;text-align:center}
.feature .icon{width:72px;height:72px;margin:0 auto;border-radius:10px}
.feature h2{margin-top:22px;font-weight:400;font-size:20px;letter-spacing:1px;color:var(--ink);white-space:nowrap}
.feature p{margin-top:8px;font-size:12.5px;line-height:16.5px;color:var(--ink-soft);letter-spacing:.3px}
.btn{display:inline-block;margin-top:15px;width:96px;height:25px;line-height:24px;font-size:11px;color:var(--white);background:linear-gradient(#7cb548,#4f8a27);border:1px solid #447a20;border-radius:2px;letter-spacing:.5px;white-space:nowrap}

.partners{left:0;top:757px;width:977px;height:140px;background:var(--band)}
.badge{background:#6f6f6f}

.footer{left:0;top:897px;width:977px;height:272px;background:linear-gradient(var(--foot-top),var(--foot-bottom))}
.col{top:53px}
.col h3{font-weight:400;font-size:17px;letter-spacing:1px;color:var(--blue-text);padding-bottom:9px;border-bottom:1px solid #555;width:155px;white-space:nowrap}
.col h3 span{color:var(--green-text)}
.col ul{list-style:none;margin-top:6px}
.col li{position:relative;padding-left:24px;height:24px;line-height:24px;font-size:10.5px;letter-spacing:1px;color:var(--white);white-space:nowrap}
.col li::before{content:"";position:absolute;left:10px;top:10px;width:5px;height:5px;border-radius:50%;background:var(--white)}
.field{left:754px;width:146px;background:var(--white);border-radius:2px;font-size:11px;color:#999;padding:6px 7px;letter-spacing:.5px}
.ok{left:866px;top:1099px;width:31px;height:29px;background:var(--blue-deep);color:var(--white);font-size:13px;text-align:center;line-height:29px;border-radius:2px}

.copyright{left:0;top:1169px;width:977px;height:31px;background:#1b9be0;color:var(--white);font-size:11px;letter-spacing:1px;text-align:center;line-height:31px}
</style>
</head>
<body>

<div class="abs topbar">
  <div class="contacts">
    <div class="contact">
      <svg width="16" height="11" viewBox="0 0 16 11"><rect x="0.5" y="0.5" width="15" height="10" fill="#fff"/><path d="M1 1l7 5 7-5" fill="none" stroke="#1fb0e4" stroke-width="1.2"/></svg>
      <span>hello@verdantcurrent.com</span>
    </div>
    <div class="contact">
      <svg width="14" height="16" viewBox="0 0 14 16"><rect width="14" height="16" rx="2" fill="#fff"/><path d="M4 3c-1 1-1 4 1 7s4 4 5 3l-1-2-2 1c-1-1-2-3-2-4l2-1z" fill="#1fb0e4"/></svg>
      <span>(03)-5550-0199</span>
    </div>
  </div>
</div>

<header class="abs header"></header>
<div class="abs brand"><span class="dot"></span><span class="name">VERDANT CURRENT</span></div>
<a class="abs social page"><span class="sq"></span>Follow our page</a>
<a class="abs social updates"><span class="sq"></span>Follow our updates</a>
<a class="abs social feed"><span class="sq"></span>Follow our RSS Feed</a>

<nav class="abs nav">
  <a style="left:17px">HOME</a>
  <a style="left:107px">ABOUT US</a>
  <a style="left:222px">TECHNOLOGIES</a>
  <a style="left:383px">OUR PRODUCTS</a>
  <a style="left:546px">CONTACT US</a>
</nav>

<div class="abs hero-shadow"></div>
<section class="abs hero">
  <svg class="abs" style="left:0;top:0" width="901" height="262">
    <circle cx="265" cy="152" r="214" fill="#fff"/>
    <defs>
      <linearGradient id="scene" x1="0" y1="0" x2="0" y2="1">
        <stop offset="0" stop-color="#0a3fa8"/><stop offset=".55" stop-color="#6fc4f2"/><stop offset=".8" stop-color="#3a78c0"/><stop offset="1" stop-color="#3f8a22"/>
      </linearGradient>
    </defs>
    <circle cx="265" cy="152" r="206" fill="url(#scene)" role="img" aria-label="Solar panels on green grass under a bright blue sky"/>
  </svg>
  <div class="abs welcome">
    <div class="kicker">WELCOME TO</div>
    <div class="name"><span class="dot"></span>VERDANT CURRENT</div>
    <p>Lorem ipsum dolor sit amet, consectetur adipiscing elit. In pretium mauris et lacus ultrices, ut iaculis urna lobortis. Vivamus vel nunc sed erat ornare tristique vitae vitae sapien.</p>
  </div>
  <div class="abs dots"><span></span><span></span><span></span><span class="on"></span></div>
</section>

<section class="abs features">
  <div class="abs divider" style="left:321px"></div>
  <div class="abs divider" style="left:581px"></div>
  <div class="abs feature" style="left:91px">
    <div class="icon" role="img" aria-label="Team icon" style="background:linear-gradient(90deg,#7cb83a,#1d9ee0,#7cb83a)"></div>
    <h2>About us</h2>
    <p>Lorem ipsum dolor sit amet, consectetur adipiscing elit. In adipiscing elit pretium mauris et lacus.</p>
    <span class="btn">Read more &rarr;</span>
  </div>
  <div class="abs feature" style="left:348px">
    <div class="icon" role="img" aria-label="Tools icon" style="background:linear-gradient(135deg,#1d9ee0,#7cb83a)"></div>
    <h2>Our Services</h2>
    <p>Lorem ipsum dolor sit amet, consectetur adipiscing elit. In adipiscing elit pretium mauris et lacus.</p>
    <span class="btn">Read more &rarr;</span>
  </div>
  <div class="abs feature" style="left:604px">
    <div class="icon" role="img" aria-label="Product box icon" style="background:#1d9ee0"></div>
    <h2>Our Products</h2>
    <p>Lorem ipsum dolor sit amet, consectetur adipiscing elit. In adipiscing elit pretium mauris et lacus.</p>
    <span class="btn">Read more &rarr;</span>
  </div>
</section>

<section class="abs partners">
  <div class="abs badge" style="left:158px;top:32px;width:72px;height:72px;border-radius:50%"></div>
  <div class="abs badge" style="left:285px;top:37px;width:40px;height:62px;border-radius:4px"></div>
  <div class="abs badge" style="left:377px;top:50px;width:134px;height:36px;border-radius:4px"></div>
  <div class="abs badge" style="left:554px;top:28px;width:96px;height:80px;border-radius:50%;background:#8a8a8a"></div>
  <div class="abs badge" style="left:704px;top:37px;width:100px;height:54px;border-radius:4px"></div>
</section>

<footer class="abs footer">
  <div class="abs col" style="left:66px">
    <h3>QUICKLINKS</h3>
    <ul><li>HOME</li><li>ABOUT US</li><li>TECHNOLOGIES</li><li>OUR PRODUCTS</li><li>CONTACT US</li></ul>
  </div>
  <div class="abs col" style="left:299px">
    <h3>ADDITIONAL <span>INFO</span></h3>
    <ul><li>FAQ</li><li>SITEMAP</li><li>PRIVACY POLICY</li><li>TERMS AND AGREEMENT</li></ul>
  </div>
  <div class="abs col" style="left:519px">
    <h3>PRODUCT <span>INFO</span></h3>
    <ul><li>PRODUCT INFORMATION</li><li>CUSTOMER SERVICE</li><li>PRODUCT WARRANTY</li><li>BRANCHES</li></ul>
  </div>
  <div class="abs col" style="left:750px">
    <h3>FREE <span>QUOTATION</span></h3>
  </div>
</footer>
<div class="abs field" style="top:976px;height:27px">Firstname</div>
<div class="abs field" style="top:1009px;height:27px">Email</div>
<div class="abs field" style="top:1042px;height:88px">Message</div>
<div class="abs ok">ok</div>

<div class="abs copyright">Copyright © 2014 VERDANT CURRENT</div>

</body>
</html>
```